Photographer website

This website will contain information to sell the services of marvello tebani an up and coming photographer based in london

Target Market(s)

SME's for corporate head shots
mums for kids parties
actors - for headshots
up and coming models

Industry/Entity Type

Photographer

Number of Pages Required

3 page

Requirements
Must have
• Home
• About me
• Contact me
• Portfolio or gallery

```html
<!DOCTYPE html>
<html lang="en">
<head>
<meta charset="utf-8">
<title>Marvello Tebani — Photographer</title>
<link rel="stylesheet" href="https://fonts.googleapis.com/css2?family=Mulish:wght@400;600;700;800&family=Dancing+Script:wght@400;600&display=swap">
<style>
  :root{
    --accent:#f29d16;
    --ink:#1d1d1d;
    --text:#3a3a3a;
    --white:#ffffff;
    --panel:rgba(20,20,20,.82);
    --dark:#1c1c1c;
    --footer:#222222;
    --line:rgba(255,255,255,.22);
    --faint:#f1f1f1;
  }
  *{box-sizing:border-box;margin:0;padding:0}
  html,body{width:1200px;height:2344px;overflow:hidden}
  body{position:relative;background:var(--white);font-family:'Mulish',sans-serif;color:var(--text)}
  .abs{position:absolute}
  .accent{color:var(--accent)}

  /* HERO */
  .hero{left:0;top:0;width:1200px;height:560px;overflow:hidden}
  .hero-photo{position:absolute;inset:0;background:
    radial-gradient(ellipse at 60% 35%,#5a5550 0%,#3a3633 40%,#252322 75%),
    linear-gradient(90deg,#2b2927,#6c6a6b);background-blend-mode:normal}
  .hero-photo::after{content:"";position:absolute;right:0;top:0;width:420px;height:560px;
    background:linear-gradient(90deg,rgba(120,118,122,0),rgba(150,145,150,.55));}
  .nav-panel{left:156px;top:47px;width:206px;height:336px;background:var(--panel);padding:28px 28px}
  .brand{display:flex;align-items:center;gap:10px;color:var(--white);font-weight:700;font-size:20px;letter-spacing:.5px;height:90px}
  .brand-dot{width:10px;height:10px;border-radius:50%;background:var(--accent)}
  .nav-list{list-style:none;margin-top:10px}
  .nav-list li{font-size:12px;letter-spacing:1.6px;color:var(--white);height:35px;line-height:35px}
  .nav-list li.active{color:var(--accent);font-weight:700;border-bottom:1px solid rgba(255,255,255,.3)}
  .nav-list li.active::before{content:"→ ";}
  .social{display:flex;gap:16px;margin-top:28px}
  .social span{width:11px;height:11px;border-radius:50%;background:#cfcfcf}
  .hero-frame{left:911px;top:250px;width:133px;height:277px;border:3px solid var(--accent)}
  .hero-title{right:181px;top:266px;text-align:right;color:var(--white);font-weight:800;font-size:50px;line-height:52px;letter-spacing:.5px}
  .hero-text{right:181px;top:444px;width:410px;text-align:right;color:var(--white);font-size:13px;line-height:17px}

  /* ABOUT */
  .about{left:0;top:560px;width:1200px;height:448px;overflow:hidden}
  .watermark{position:absolute;font-weight:700;color:var(--faint);white-space:nowrap}
  .about .watermark{right:30px;top:60px;font-size:150px;letter-spacing:4px}
  .about-photo{left:156px;top:65px;width:280px;height:319px;background:radial-gradient(circle at 50% 55%,#5a4a3a 0%,#2d2a33 45%,#15131a 100%)}
  .section-title{font-size:25px;font-weight:400;color:var(--ink);letter-spacing:.5px}
  .about-title{left:512px;top:56px}
  .about-lead{left:512px;top:113px;width:420px;font-weight:700;font-size:14px;line-height:19px;color:var(--ink)}
  .about-body{left:512px;top:165px;width:530px;font-size:12.5px;line-height:17.5px;color:var(--text)}
  .about-body p+p{margin-top:17px}
  .btn-outline{display:flex;align-items:center;justify-content:center;gap:6px;border:1px solid #9a9a9a;border-left:5px solid var(--accent);font-size:11.5px;color:var(--ink);height:31px;width:128px}
  .about-btn{left:512px;top:310px;background:var(--white)}

  /* GALLERY */
  .gallery{left:0;top:1008px;width:1200px;height:664px;background:linear-gradient(180deg,#4d5446 0%,#6d7a55 25%,#4f5a36 60%,#3d4a22 100%)}
  .gallery-title{left:0;width:1200px;top:55px;text-align:center;color:var(--white)}
  .tile{position:absolute}
  .t1{left:0;top:122px;width:367px;height:203px;background:linear-gradient(135deg,#c9c9c9,#6a6a6a)}
  .t2{left:0;top:333px;width:367px;height:203px;background:linear-gradient(135deg,#e6e6e6,#7a7a7a)}
  .t3{left:377px;top:122px;width:371px;height:414px;background:linear-gradient(160deg,#7c9560,#d9c7b2 55%,#eee)}
  .t4{left:756px;top:122px;width:444px;height:203px;background:linear-gradient(180deg,#d8d8d8,#5a5a5a)}
  .t5{left:756px;top:333px;width:211px;height:203px;background:linear-gradient(180deg,#a8a8a8,#4a4a4a)}
  .t6{left:977px;top:333px;width:223px;height:203px;background:linear-gradient(135deg,#5e5e5e,#2a2a2a)}
  .caption{left:377px;top:458px;width:371px;height:78px;background:var(--accent);color:var(--white);padding:0 22px;display:flex;align-items:center;justify-content:space-between}
  .caption-name{font-size:12.5px;font-weight:600;line-height:16px;width:160px}
  .caption-actions{display:flex;gap:12px}
  .round-btn{width:38px;height:38px;border-radius:50%;background:var(--ink);display:flex;align-items:center;justify-content:center}
  .view-all{left:536px;top:569px;color:var(--white);border-color:var(--white);background:transparent}

  /* QUOTE */
  .quote{left:0;top:1672px;width:1200px;height:200px;overflow:hidden;background:var(--white)}
  .quote .watermark{left:30px;top:0;font-size:170px}
  .quote-line{left:0;width:1200px;text-align:center;font-family:'Dancing Script',cursive;color:var(--ink)}
  .q1{top:30px;font-size:33px}
  .q2{top:72px;font-size:24px}
  .btn-solid{display:flex;align-items:center;justify-content:center;gap:6px;background:var(--accent);color:var(--white);font-size:11.5px;height:31px;width:128px}
  .contact-btn{left:536px;top:128px}

  /* CONTACT */
  .contact{left:0;top:1872px;width:1200px;height:409px;background:radial-gradient(ellipse at 50% 60%,#3b3b3b 0%,#262626 45%,#1a1a1a 100%)}
  .contact-title{left:0;width:1200px;top:42px;text-align:center;color:var(--white)}
  .field{position:absolute;border-bottom:1px solid var(--line);color:#d9d9d9;font-size:12.5px;padding:0 0 8px 16px;height:22px}
  .f-first{left:156px;top:101px;width:435px}
  .f-mail{left:625px;top:101px;width:419px}
  .f-phone{left:156px;top:159px;width:435px}
  .f-city{left:625px;top:159px;width:419px}
  .f-msg{left:156px;top:222px;width:888px;height:78px;border:1px solid var(--line);padding:14px 16px}
  .send-btn{left:156px;top:333px}

  /* FOOTER */
  .footer{left:0;top:2281px;width:1200px;height:63px;background:var(--footer)}
  .copy{left:156px;top:22px;color:#d5d5d5;font-size:11.5px}
  .foot-nav{right:156px;top:14px;display:flex;gap:18px;font-size:11.5px;color:#e0e0e0}
  .foot-social{right:156px;top:37px;display:flex;gap:14px}
  .foot-social span{width:9px;height:9px;border-radius:50%;background:#bdbdbd}
</style>
</head>
<body>

<header class="hero abs">
  <div class="hero-photo" role="img" aria-label="Photographer holding a camera on a city street"></div>
  <nav class="nav-panel abs">
    <div class="brand"><span class="brand-dot"></span>Tebani Studio</div>
    <ul class="nav-list">
      <li class="active">Home</li>
      <li>About me</li>
      <li>My Portfolio</li>
      <li>Contact me</li>
    </ul>
    <div class="social"><span></span><span></span><span></span><span></span><span></span></div>
  </nav>
  <div class="hero-frame abs"></div>
  <h1 class="hero-title abs">HI<br>I'M TOPPIC<br>PHOTOGRAPHER</h1>
  <p class="hero-text abs">I specialise in portraiture photography. My first few years behind the camera is when I fell in love with this particular type of photography.</p>
</header>

<section class="about abs">
  <div class="watermark">Tebani</div>
  <div class="about-photo abs" role="img" aria-label="Hand holding a camera lens reflecting city lights"></div>
  <h2 class="section-title about-title abs">About <span class="accent">Me</span></h2>
  <p class="about-lead abs">Hi My name is <span class="accent">Marvello Tebani</span> Born in East Brazil, grew up in Spain.</p>
  <div class="about-body abs">
    <p>I now live in London but I travel internationally for work.<br>When traveling around the globe I'm always looking for the perfect setting to create that special Picture. My goal is to show that little part that can't be appreciated on the naked eye alone.</p>
    <p>I'm incredibly well traveled sometimes shy in the crowds but very curious and enthusiastic of people and their imagery.</p>
  </div>
  <div class="btn-outline about-btn abs">Explore More <span>»</span></div>
</section>

<section class="gallery abs" role="img" aria-label="Blurred green meadow background">
  <h2 class="section-title gallery-title abs">My Awsome <span class="accent">Gallery</span></h2>
  <div class="tile t1" role="img" aria-label="Photographer lying on the ground shooting, black and white"></div>
  <div class="tile t2" role="img" aria-label="Bird perched on a camera lens, black and white"></div>
  <div class="tile t3" role="img" aria-label="Wedding couple embracing"></div>
  <div class="tile t4" role="img" aria-label="Wooden pier over the sea, black and white"></div>
  <div class="tile t5" role="img" aria-label="Person walking on rail tracks with a camera"></div>
  <div class="tile t6" role="img" aria-label="Bokeh lights on branches"></div>
  <div class="caption abs">
    <span class="caption-name">Lorium Photograph Dummy name</span>
    <div class="caption-actions">
      <span class="round-btn"><svg width="14" height="14" viewBox="0 0 14 14" fill="none" stroke="#fff" stroke-width="1.6"><path d="M2 12L12 2M8 2h4v4M6 12H2V8"/></svg></span>
      <span class="round-btn"><svg width="14" height="14" viewBox="0 0 14 14" fill="none" stroke="#fff" stroke-width="1.6"><circle cx="4.5" cy="9.5" r="2.5"/><circle cx="9.5" cy="4.5" r="2.5"/><path d="M5.5 8.5l3-3"/></svg></span>
    </div>
  </div>
  <div class="btn-outline view-all abs">View All <span>»</span></div>
</section>

<section class="quote abs">
  <div class="watermark">Tebani</div>
  <p class="quote-line q1 abs">I don't take Photographs, I Make it <span class="accent">live...</span></p>
  <p class="quote-line q2 abs">Let us <span class="accent">Freeze</span> your Expressions forever...</p>
  <div class="btn-solid contact-btn abs">Contact Me <span>»</span></div>
</section>

<section class="contact abs" role="img" aria-label="Dark close-up of a camera lens">
  <h2 class="section-title contact-title abs">Contact <span class="accent">Form</span></h2>
  <div class="field f-first">First name :</div>
  <div class="field f-mail">E-mail address :</div>
  <div class="field f-phone">Phone :</div>
  <div class="field f-city">City :</div>
  <div class="field f-msg">Message :</div>
  <div class="btn-solid send-btn abs">Send
    <svg width="12" height="12" viewBox="0 0 12 12" fill="none" stroke="#fff" stroke-width="1.3"><path d="M1 6l10-5-3 10-2-4z"/></svg>
  </div>
</section>

<footer class="footer abs">
  <p class="copy abs">© 2016 <span class="accent">Marvello Tebani</span>. All Rights Reserved.</p>
  <div class="foot-nav abs"><span class="accent">Home</span><span>About me</span><span>My Portfolio</span><span>Contact me</span></div>
  <div class="foot-social abs"><span></span><span></span><span></span><span></span><span></span></div>
</footer>

</body>
</html>
```